Professional Bio Dean Forsyth

Hello,
Can you please create a templated for a professional Bio?
I would like to be able to drop in a photo, information on the title, and text about the person. Please add our logo as well. Here is the photo for the person this is for.
Below is an example.

```html
<!DOCTYPE html>
<html lang="en">
<head>
<meta charset="utf-8">
<title>Professional Bio – Nathan Whitlock</title>
<link rel="stylesheet" href="https://fonts.googleapis.com/css2?family=Raleway:wght@400;500;700&display=swap">
<style>
  :root {
    --navy: #2d3b77;
    --band-grey: #d9dbdc;
    --paper: #ffffff;
    --backdrop: #eceded;
    --body-text: #3a3a3a;
  }
  * { margin: 0; padding: 0; box-sizing: border-box; }
  html, body {
    width: 1200px;
    height: 1200px;
    overflow: hidden;
    background: var(--backdrop);
    font-family: "Raleway", sans-serif;
  }
  .bio-sheet {
    position: absolute;
    left: 152px;
    top: 20px;
    width: 1026px;
    height: 1328px;
    background: var(--paper);
    transform: scale(0.8735);
    transform-origin: top left;
    overflow: hidden;
  }
  .header-bands {
    position: absolute;
    left: 0;
    top: 0;
    width: 1026px;
    height: 330px;
  }
  .brand-name {
    position: absolute;
    left: 84px;
    top: 100px;
    width: 217px;
    text-align: center;
    color: var(--paper);
    font-weight: 700;
    font-size: 38px;
    line-height: 1.15;
    letter-spacing: 3px;
  }
  .portrait {
    position: absolute;
    left: 742px;
    top: 174px;
    width: 203px;
    height: 266px;
    background: linear-gradient(180deg, #55585c 0%, #3e4146 55%, #27315a 100%);
  }
  .person-name {
    position: absolute;
    left: 82px;
    top: 378px;
    color: var(--navy);
    font-weight: 400;
    font-size: 60px;
    line-height: 1;
    white-space: nowrap;
  }
  .role-list {
    position: absolute;
    left: 85px;
    top: 468px;
    list-style: none;
    color: var(--navy);
    font-weight: 700;
    font-size: 20px;
    line-height: 28px;
  }
  .role-list .role-spaced { letter-spacing: 2.4px; word-spacing: 6px; }
  .bio-text {
    position: absolute;
    left: 84px;
    top: 590px;
    width: 858px;
    color: var(--body-text);
    font-size: 16.4px;
    line-height: 23.3px;
    text-align: justify;
  }
  .bio-text p + p { margin-top: 23.3px; }
</style>
</head>
<body>
  <article class="bio-sheet">
    <svg class="header-bands" viewBox="0 0 1026 330" aria-hidden="true">
      <polygon points="585,166 1026,52 1026,262" fill="var(--band-grey)"/>
      <polygon points="0,0 1026,0 1026,52 0,318" fill="var(--navy)"/>
    </svg>

    <div class="brand-name">HARLOW GLASS</div>

    <div class="portrait" role="img" aria-label="Headshot portrait of Nathan Whitlock in a navy blazer against a grey studio backdrop"></div>

    <h1 class="person-name">Nathan Whitlock, P.E.</h1>

    <ul class="role-list">
      <li>Senior Managing Partner: Harlow Glass, Inc</li>
      <li class="role-spaced">CEO &amp; Founder: HGS Service, LLC</li>
      <li>Founder: Ridgeline Metals, LLC</li>
    </ul>

    <section class="bio-text">
      <p>Nate grew up in beautiful Colorado. From his very early days, he loved building things and tinkering with everything. Nate graduated from Ridgeview High School in Littleton and from Front Range University, where he earned his B.S. in Architectural Engineering with an emphasis in Construction Management.</p>
      <p>While in college, Nate wanted construction experience "in the field" with the very work and the very people that he hoped to lead. Scanning the newspaper for summer jobs, a chance want-ad led him to a startup construction company in Denver called Harlow Glass, then specializing in skylights and glass storefronts. Nate not only gained the field experience he was looking for but a lifelong friend, Dean Forsyth. In Dean, Nate saw the same passion he had for building things and building people. They became business partners in 2009 and have since grown the company together 10x.</p>
      <p>Nate's primary responsibility at Harlow Glass is to champion its thousand-year vision of "Bringing Light Inside". Ultimately, this means helping to improve and inspire the lives of its customers and team members – for a long time. Today, Harlow Glass designs, manufactures and installs the exterior glass systems on monumental buildings, operating in 5 states, and is one of the best glaziers anywhere. Never willing to rest on its laurels, the company sought a way to keep improving and found Kaizen Motors. In 2017, Harlow Glass established a close partnership with Kaizen Motors/UK to learn their way and today is fortunate enough to be their #1 protege. Nate was a founder of Harlow Glass's Elite Team, an intense leadership program for Harlow Glass team members, Summit, a crazy, no-holds-barred executive program, and its college Internship Program, where the company continuously seeds the next generation. With his continued thirst for building things and building people, Nate started HGS Service in 2013 and Ridgeline Metals in 2022.</p>
      <p>Together with his wife Elena, Nate enjoys climbing, hiking, alpinism/mountaineering and raising their 2 kids. They gleefully thrive on the challenge of teaching their 3-year-old and 7-year-old how to grow their bodies, minds and sprits. Nate enjoys supporting his community, having a soft spot for kids. He enjoys striving for his book-a-week target (his favorite book is The Long Ascent), snowboarding, hunting, learning the trumpet, and making furniture in his shop.</p>
    </section>
  </article>
</body>
</html>
```